Financial consulting firm
Norvale Advisory
Project: Financial consulting firm
Financial consulting firm - Financial Services
Creative Brief
Professional
Marcus T. Delford
2870 Kapena Lane, Suite 406 Honolulu, HI 96813
marcus@norvaleadvisory.com
www.norvaleadvisory.com
Logo & website address

```html
<!DOCTYPE html>
<html lang="en">
<head>
<meta charset="utf-8">
<title>Norvale Advisory – Stationery Set</title>
<link href="https://fonts.googleapis.com/css2?family=Cormorant+Garamond:wght@600&family=Lato:wght@400;700&display=swap" rel="stylesheet">
<style>
  :root{
    --navy:#2f2e6e;
    --grey:#8b8d97;
    --grey-light:#c9cad0;
    --paper:#ffffff;
    --ink:#3a3a48;
    --bg:#e9e6e0;
  }
  *{box-sizing:border-box;margin:0;padding:0}
  html,body{width:1200px;height:247px;overflow:hidden;background:var(--bg)}
  body{position:relative;font-family:"Lato",sans-serif;color:var(--ink)}
  .piece{position:absolute;background:var(--paper);box-shadow:0 1px 3px rgba(0,0,0,.18);overflow:hidden}
  .brand{display:flex;align-items:center;gap:3px;font-family:"Cormorant Garamond",serif;font-weight:600;color:var(--navy);line-height:1;white-space:nowrap}
  .brand .mark{background:var(--navy);flex:none}
  .brand.on-dark{color:var(--paper)}
  .brand.on-dark .mark{background:var(--paper)}
  .tiny{font-size:3px;line-height:1.4;white-space:nowrap}

  /* logo panel */
  .logo-panel{left:10px;top:10px;width:100px;height:118px;display:flex;flex-direction:column;align-items:center;justify-content:center;gap:6px}
  .logo-panel .brand{font-size:24px;gap:4px}
  .logo-panel .brand .mark{width:11px;height:11px}
  .logo-panel .tag{font-size:5px;letter-spacing:.5px;color:var(--grey);white-space:nowrap}

  /* business cards */
  .card{width:50px;height:30px;padding:4px}
  .card.navy{background:var(--navy)}
  .card.grey{background:var(--grey)}
  .card .brand{font-size:8px}
  .card .brand .mark{width:4px;height:4px}
  .card-front{left:10px;top:170px}
  .card-back{left:64px;top:170px}
  .card-front2{left:10px;top:205px}
  .card-back2{left:64px;top:205px}
  .card .name{font-size:3.6px;font-weight:700;color:var(--navy);white-space:nowrap}

  /* letterheads */
  .letter{width:108px;height:186px;top:22px;padding:10px}
  .letter-a{left:228px}
  .letter-b{left:350px}
  .letter .brand{font-size:11px;justify-content:flex-end}
  .letter .brand .mark{width:6px;height:6px}
  .letter .body{margin-top:26px}
  .letter .body p{margin-bottom:4px}
  .letter .sign{margin-top:30px;font-size:5px;font-style:italic;color:var(--navy);white-space:nowrap}
  .letter .foot{position:absolute;left:10px;right:10px;bottom:8px;text-align:center;border-top:.5px solid var(--grey-light);padding-top:2px;font-size:2.6px}

  /* small cards */
  .biz{left:474px;top:96px;width:62px;height:36px;padding:5px}
  .biz .brand{font-size:8px}
  .biz .brand .mark{width:4px;height:4px}
  .slip{left:474px;top:150px;width:62px;height:36px;padding:5px}
  .slip .brand{font-size:8px}
  .slip .brand .mark{width:4px;height:4px}
  .slip .band{position:absolute;left:0;right:0;bottom:0;height:6px;background:var(--navy)}

  /* envelopes */
  .env{width:140px;left:556px}
  .env-top{top:22px;height:30px;background:var(--grey-light)}
  .env-flap{top:56px;height:30px;background:var(--navy)}
  .env-flap svg,.env-back svg{position:absolute;inset:0}
  .env-front{top:104px;height:50px;padding:5px}
  .env-front .brand{font-size:9px}
  .env-front .brand .mark{width:5px;height:5px}
  .env-back{top:164px;height:40px}

  /* folder */
  .folder-inside{left:760px;top:22px;width:190px;height:186px}
  .folder-inside .pocket{position:absolute;left:0;right:0;bottom:0;height:64px;background:var(--navy)}
  .folder-inside .pocket svg{position:absolute;left:0;top:-12px}
  .folder-cover{left:956px;top:22px;width:150px;height:186px;background:var(--navy);display:flex;flex-direction:column;align-items:center;padding-top:34px;gap:5px}
  .folder-cover .brand{font-size:20px;gap:4px}
  .folder-cover .brand .mark{width:10px;height:10px}
  .folder-cover .tag{font-size:5px;color:var(--grey-light);letter-spacing:.5px;white-space:nowrap}
  .folder-cover .web{position:absolute;bottom:10px;font-size:4px;color:var(--grey-light);white-space:nowrap}
</style>
</head>
<body>

<div class="piece logo-panel">
  <div class="brand"><span class="mark"></span>Norvale</div>
  <div class="tag">Financial Consulting</div>
</div>

<div class="piece card navy card-front">
  <div class="brand on-dark"><span class="mark"></span>Norvale</div>
</div>
<div class="piece card grey card-back">
  <div class="tiny" style="color:#fff">Marcus T. Delford<br>(808) 555-0147</div>
</div>
<div class="piece card grey card-front2">
  <div class="brand on-dark"><span class="mark"></span>Norvale</div>
</div>
<div class="piece card card-back2">
  <div class="name">Marcus T. Delford</div>
  <div class="tiny">marcus@norvaleadvisory.com<br>www.norvaleadvisory.com</div>
</div>

<div class="piece letter letter-a">
  <div class="brand"><span class="mark"></span>Norvale Advisory</div>
  <div class="body tiny">
    <p>Dear Client,</p>
    <p>Thank you for choosing us as your financial partner.</p>
    <p>We look forward to planning your next steps.</p>
    <p>Sincerely,</p>
  </div>
  <div class="sign">Marcus T. Delford</div>
  <div class="foot tiny">2870 Kapena Lane, Suite 406 Honolulu, HI 96813<br>www.norvaleadvisory.com</div>
</div>

<div class="piece letter letter-b">
  <div class="brand"><span class="mark"></span>Norvale Advisory</div>
  <div class="body tiny">
    <p>Dear Client,</p>
    <p>Thank you for choosing us as your financial partner.</p>
    <p>We look forward to planning your next steps.</p>
    <p>Sincerely,</p>
  </div>
  <div class="sign">Marcus T. Delford</div>
  <div class="foot tiny">marcus@norvaleadvisory.com · (808) 555-0147</div>
</div>

<div class="piece biz">
  <div class="brand"><span class="mark"></span>Norvale Advisory</div>
  <div class="tiny" style="margin-top:4px">Marcus T. Delford<br>marcus@norvaleadvisory.com</div>
</div>
<div class="piece slip">
  <div class="brand"><span class="mark"></span>Norvale Advisory</div>
  <div class="band"></div>
</div>

<div class="piece env env-top"></div>
<div class="piece env env-flap">
  <svg width="140" height="30" viewBox="0 0 140 30"><path d="M0 0 L70 24 L140 0" fill="none" stroke="#8b8d97" stroke-width="1"/></svg>
</div>
<div class="piece env env-front">
  <div class="brand"><span class="mark"></span>Norvale Advisory</div>
  <div class="tiny" style="margin-top:3px">2870 Kapena Lane, Suite 406<br>Honolulu, HI 96813</div>
</div>
<div class="piece env env-back">
  <svg width="140" height="40" viewBox="0 0 140 40"><path d="M0 0 L70 28 L140 0" fill="none" stroke="#c9cad0" stroke-width="1"/></svg>
</div>

<div class="piece folder-inside">
  <div class="pocket">
    <svg width="190" height="14" viewBox="0 0 190 14"><path d="M0 12 Q95 0 190 12 L190 14 L0 14Z" fill="#2f2e6e"/></svg>
  </div>
</div>
<div class="piece folder-cover">
  <div class="brand on-dark"><span class="mark"></span>Norvale</div>
  <div class="tag">Financial Consulting</div>
  <div class="web">www.norvaleadvisory.com</div>
</div>

</body>
</html>
```